Sydney law firm, Prestwicks Solicitors, needs a flyer design!

We need a flyer design for our law firm which has been operating in Sydney for over 35 years. We want to send the flyer out to potential clients and also to existing clients to let them know the range of services that we provide. Our corporate colours are white, red and black and we would like these incorporated somewhat. The final design should be clean, modern and professional.

We would like the design to fit a double sided flyer approx. 210mm high x 100mm wide.

Industry/Entity Type

Law Firm

Font styles to use
Serif
Sans Serif

Colors
eb2026
ffffff

Requirements
Must have
• Details needed on the flyer are:
• Prestwicks Solicitors
• 3/82 Carradine Street, Liverpool, NSW 2170
• (02) 9418 3562
• www.prestwickssolicitors-example.com.au
• info@prestwickssolicitors-example.com.au
• Our areas of practice include:
• Property Law
• Conveyancing
• Leases
• Criminal Law
• Family Law
• Litigation and Dispute Resolution
• Company Law
• Wills and Estates
• Powers of Attorney and Guardianship
Should not have
• a picture of scales or a picture of a gavel

```html
<!DOCTYPE html>
<html lang="en">
<head>
<meta charset="utf-8">
<title>Prestwicks Solicitors – Flyer</title>
<link rel="stylesheet" href="https://fonts.googleapis.com/css2?family=Bebas+Neue&display=swap">
<style>
  :root {
    --brand-red: #c8272b;
    --ink: #1c1c1c;
    --grey-text: #5a5a5a;
    --paper-top: #ffffff;
    --paper-bottom: #e4e4e4;
    --white: #ffffff;
  }
  html, body {
    margin: 0;
    padding: 0;
    width: 1200px;
    height: 1131px;
    overflow: hidden;
    background: var(--white);
  }
  body {
    position: relative;
    font-family: "Bebas Neue", "Arial Narrow", sans-serif;
  }
  .flyer {
    position: absolute;
    top: 22px;
    width: 506px;
    height: 1068px;
    background: linear-gradient(180deg, var(--paper-top) 0%, #f3f3f3 55%, var(--paper-bottom) 100%);
    box-shadow: 0 0 6px rgba(0,0,0,0.18);
    overflow: hidden;
  }
  .flyer--front { left: 35px; }
  .flyer--back { left: 635px; }
  .flyer__shapes {
    position: absolute;
    inset: 0;
    width: 100%;
    height: 100%;
  }
  .line {
    position: absolute;
    left: 0;
    width: 100%;
    text-align: center;
    line-height: 1;
    transform: translateY(-50%);
    white-space: nowrap;
  }
  .headline { font-size: 46px; color: var(--ink); }
  .headline--accent { color: var(--brand-red); }
  .tagline { font-size: 28px; color: var(--ink); }
  .brand-name {
    font-size: 50px;
    letter-spacing: 3px;
    color: var(--ink);
  }
  .brand-sub {
    font-size: 22px;
    letter-spacing: 14px;
    color: var(--ink);
  }
  .web-address { font-size: 25px; color: var(--white); }
  .practice-heading { font-size: 26px; color: var(--grey-text); }
  .practice-item { font-size: 28px; color: var(--grey-text); }
  .contact-line { font-size: 24px; color: var(--grey-text); }
</style>
</head>
<body>

  <section class="flyer flyer--front">
    <svg class="flyer__shapes" viewBox="0 0 405 854" preserveAspectRatio="none">
      <defs>
        <linearGradient id="clientPhotoTones" x1="0" y1="0" x2="1" y2="1">
          <stop offset="0" stop-color="#b9cfe0"/>
          <stop offset="0.5" stop-color="#d8c9b5"/>
          <stop offset="1" stop-color="#eeeae4"/>
        </linearGradient>
      </defs>
      <polygon points="0,127 405,208 405,226 0,145" fill="var(--brand-red)"/>
      <polygon points="0,150 405,230 405,533 0,582" fill="url(#clientPhotoTones)" role="img" aria-label="Photo of a smiling senior couple shaking hands with their solicitor"/>
      <polygon points="0,580 405,530 405,548 0,600" fill="var(--brand-red)"/>
      <polygon points="0,786 405,804 405,810 0,792" fill="var(--brand-red)"/>
      <polygon points="0,792 405,810 405,854 0,854" fill="var(--ink)"/>
    </svg>

    <div class="line headline" style="top:68px">When you feel supported,</div>
    <div class="line headline headline--accent" style="top:113px">The life is more easier</div>

    <div class="line tagline" style="top:775px">So we put all our experience</div>
    <div class="line tagline" style="top:808px">as lawyers at your service</div>

    <div class="line brand-name" style="top:899px">Prestwicks</div>
    <div class="line brand-sub" style="top:946px">Solicitors</div>

    <div class="line web-address" style="top:1042px">www.prestwickssolicitors-example.com.au</div>
  </section>

  <section class="flyer flyer--back">
    <svg class="flyer__shapes" viewBox="0 0 405 854" preserveAspectRatio="none">
      <defs>
        <linearGradient id="familyPhotoTones" x1="0" y1="0" x2="1" y2="1">
          <stop offset="0" stop-color="#5f7d4a"/>
          <stop offset="0.45" stop-color="#d9a99a"/>
          <stop offset="1" stop-color="#8c8f95"/>
        </linearGradient>
      </defs>
      <rect x="0" y="0" width="405" height="240" fill="url(#familyPhotoTones)" role="img" aria-label="Photo of a happy young family with two children piggybacking"/>
      <polygon points="0,226 405,236 405,254 0,244" fill="var(--ink)"/>
      <polygon points="0,788 405,804 405,810 0,794" fill="var(--ink)"/>
      <polygon points="0,794 405,810 405,854 0,854" fill="var(--brand-red)"/>
    </svg>

    <div class="line practice-heading" style="top:344px">Our areas of practice include:</div>
    <div class="line practice-item" style="top:390px">- Property Law</div>
    <div class="line practice-item" style="top:422px">- Conveyancing</div>
    <div class="line practice-item" style="top:455px">- Leases</div>
    <div class="line practice-item" style="top:487px">- Criminal Law</div>
    <div class="line practice-item" style="top:520px">- Family Law</div>
    <div class="line practice-item" style="top:552px">- Litigation and Dispute Resolution</div>
    <div class="line practice-item" style="top:585px">- Company Law</div>
    <div class="line practice-item" style="top:617px">- Wills and Estates</div>
    <div class="line practice-item" style="top:650px">- Powers of Attorney and Guardianship</div>

    <div class="line contact-line" style="top:728px">3/82 Carradine Street, Liverpool, NSW 2170</div>
    <div class="line contact-line" style="top:756px">- (02) 9418 3562</div>
    <div class="line contact-line" style="top:784px">info@prestwickssolicitors-example.com.au</div>

    <div class="line brand-name" style="top:899px">Prestwicks</div>
    <div class="line brand-sub" style="top:946px">Solicitors</div>

    <div class="line web-address" style="top:1042px">www.prestwickssolicitors-example.com.au</div>
  </section>

</body>
</html>
```